Website design for Tallow Ridge Trading Inc

We are looking to build a website for our company. We are a scrap metal recycling company based out of Los Angeles. We purchase scrap metal in the US and ship them to China for recycling into fresh metal ores to supply industrial users. We would designs that emphasize the color green given our name and the nature of our business. Recycling themes are welcomed. We already have a URL at:
http://tallowridgetradinginc.example/
At this point, I would like 4 pages:
- Home page
- About Us
- Resources
- Contact us
Our sister company is Marrow Peak Intl Inc and they have a website that we can use as a starting point.
http://www.marrowpeak-intl.example/
Our competitor has a website below. However we dislike the design given we believe it looks rather dull.
http://www.vesperalloyworks.example/en/
Lastly, this is for a website shell only. Please design the template, graphics, and color schemes. We will write the contents later.

```html
<!DOCTYPE html>
<html lang="en">
<head>
<meta charset="utf-8">
<title>Tallow Ridge Trading Inc — Home</title>
<link rel="stylesheet" href="https://fonts.googleapis.com/css2?family=Questrial&family=Didact+Gothic&display=swap">
<style>
  :root {
    --page-bg: #ffffff;
    --sheet-bg: #f3f3f3;
    --nav-bg: #ebebeb;
    --nav-edge: #c9c9c9;
    --brand-green: #6cbf4f;
    --rule-green: #7cc56a;
    --rule-grey: #8a8a8a;
    --ink: #3a3a3a;
    --ink-soft: #555555;
    --hill-dark: #1f3a12;
    --hill-mid: #3f6e22;
    --hill-light: #79a84a;
    --sky: #bfd8d8;
    --water-light: #3aa0a3;
    --water-dark: #0c2c36;
  }
  html, body {
    margin: 0;
    width: 1200px;
    height: 900px;
    overflow: hidden;
    background: var(--page-bg);
  }
  .canvas {
    position: relative;
    width: 1200px;
    height: 900px;
    overflow: hidden;
  }
  .sheet {
    position: absolute;
    left: 260px;
    top: 0;
    width: 720px;
    height: 900px;
    background: var(--sheet-bg);
    box-shadow: 2px 0 3px rgba(0,0,0,0.12);
  }
  .brand {
    position: absolute;
    left: 260px;
    width: 720px;
    top: 38px;
    text-align: center;
  }
  .brand-mark {
    display: block;
    margin: 0 auto 8px;
    width: 26px;
    height: 26px;
    border-radius: 50%;
    background: var(--brand-green);
    position: relative;
    left: 13px;
  }
  .brand-name {
    font-family: "Questrial", sans-serif;
    font-size: 30px;
    letter-spacing: 0.5px;
    color: var(--brand-green);
    line-height: 1;
    text-transform: lowercase;
  }
  .main-nav {
    position: absolute;
    left: 293px;
    top: 153px;
    width: 650px;
    height: 52px;
    background: var(--nav-bg);
    border: 1px solid var(--nav-edge);
    border-left-color: #e0e0e0;
    border-top-color: #e0e0e0;
    display: flex;
    box-sizing: content-box;
  }
  .nav-item {
    font-family: "Questrial", sans-serif;
    font-size: 20px;
    color: var(--ink);
    text-decoration: none;
    display: flex;
    align-items: center;
    justify-content: center;
    height: 100%;
    position: relative;
  }
  .nav-item + .nav-item::before {
    content: "";
    position: absolute;
    left: 0;
    top: 7px;
    bottom: 7px;
    width: 2px;
    background: var(--brand-green);
  }
  .nav-home { width: 153px; }
  .nav-about { width: 174px; font-variant: small-caps; }
  .nav-resources { width: 181px; }
  .nav-contact { width: 142px; font-variant: small-caps; }
  .rule {
    position: absolute;
    left: 293px;
    width: 652px;
    height: 0;
  }
  .rule-top { top: 241px; border-top: 2px solid var(--rule-green); }
  .rule-bottom { top: 818px; border-top: 1px solid var(--rule-grey); }
  .hero-band {
    position: absolute;
    left: 0;
    top: 289px;
    width: 1200px;
    height: 226px;
    background:
      linear-gradient(90deg, rgba(200,225,225,0.75) 0%, rgba(200,225,225,0.25) 12%, rgba(0,0,0,0) 25%, rgba(0,0,0,0) 85%, rgba(0,0,0,0.2) 100%),
      linear-gradient(180deg, var(--sky) 0%, var(--hill-dark) 8%, var(--hill-mid) 38%, var(--hill-light) 58%, var(--water-light) 62%, #1c5b68 75%, var(--water-dark) 100%);
    box-shadow: 0 2px 3px rgba(0,0,0,0.2);
  }
  .intro {
    position: absolute;
    left: 300px;
    top: 592px;
    width: 640px;
    margin: 0;
    font-family: "Didact Gothic", sans-serif;
    font-size: 22.5px;
    line-height: 32.5px;
    letter-spacing: 1.1px;
    word-spacing: 3px;
    color: var(--ink);
    text-align: center;
  }
  .footer-note {
    position: absolute;
    left: 260px;
    width: 720px;
    top: 846px;
    text-align: center;
    font-family: "Didact Gothic", sans-serif;
    font-size: 11px;
    color: var(--ink-soft);
    word-spacing: 2px;
  }
</style>
</head>
<body>
<div class="canvas">
  <div class="sheet"></div>

  <header class="brand">
    <span class="brand-mark" aria-hidden="true"></span>
    <div class="brand-name">Tallow Ridge Trading Inc</div>
  </header>

  <nav class="main-nav">
    <a class="nav-item nav-home" href="#">Home</a>
    <a class="nav-item nav-about" href="#">About us</a>
    <a class="nav-item nav-resources" href="#">Resources</a>
    <a class="nav-item nav-contact" href="#">Contact us</a>
  </nav>

  <div class="rule rule-top"></div>

  <div class="hero-band" role="img" aria-label="Panoramic photo of green wooded hills around a calm turquoise lake"></div>

  <p class="intro">At tallowridgetrading, we strongly believe in being an honest and trustworthy business partner to each and every one of our clients. We are committed to always putting our clients' interests first (sample)</p>

  <div class="rule rule-bottom"></div>

  <footer class="footer-note">copyright information</footer>
</div>
</body>
</html>
```